Uncoded front page web design for wedding and event planning company

Hi.

I am launching a wedding and event planning company called Silver Fern Gatherings and need a professional and appealing web design.

So, let me explain my company. I am based in Swindon in Wiltshire but the company will plan weddings and events in Oxfordshire, Wiltshire, Berkshire and London.

We will plan weddings, birthdays, conferences, product launches, fashion shows and conventions but the main focus of the website at this stage should be the weddings with all the other occasions being covered under a single 'events' heading.

My contact details for the website should be:
Marion Blake
marion@silverferngatherings.co.uk
01632 960457 / 07700 900583

I'd like the website to feel clean, bright and elegant and be set against a white or off-white background. My logo is purple and I'd therefore like some purple incorporated into the design although feel free to use a more muted purple as my one might be a little bright? I'm also considering whether it would look nice paired with a little of the colour gold - maybe as a font colour in places?? I'll leave you to figure that one out as your design eye will be better than mine but for your reference below is my purple colour and my suggested gold one....

My purple colour is Pantone 2592 C but feel free to use others
My suggested gold I'm looking at is Pantone 14-1041 TCX

I would like to incorporate a Facebook feed in the front page if possible, if it looks right. I'd also like to include a variety of pictures as well so I've included a few in a Dropbox folder which is linked below. Please don't feel obliged to use them all by any means (there's loads!) but you've got a few there to play with. If you find any other royalty free images you'd rather use please go ahead but on the understanding I can have them afterwards!

My logo can be retrieved via this Dropbox link...
You'll notice there are 2 styles of placement. Please feel free to use either to fit in with your design...
https://www.filedrawer-example.com/sh/qk7pa2mwx9rn4lt/BBBKzq8ohPnvve4S03LoPjvb?dl=0

The wedding images I have are in this Dropbox folder...
https://www.filedrawer-example.com/sh/m8wd6rzp2lo4ye1/BBB4kqrXv8nWd7S05JmOgtlp?dl=0

Other than that, it's over to you.... I can't wait to receive your designs :-)

Ooh....finally just to say, as I receive designs in I think I'll notice aspects that I like and don't like and if I feel they'll be useful for other designers, I'll update my brief below. Thanks

BRIEF UPDATE:
Someone asked if I had a tag-line. Could you use "Creating exquisite occasions today for amazing memories tomorrow"

I realise I hadn't explained what I'd like included on my home page so here's some notes to consider....

A welcome to section for me to start narrative about us and our services which has a button that links to our 'about us' page and 'services' page for further information.

A section that nicely illustrates what services we offer whether that be with icons or pictures.

A section with some photos in that would link to our gallery

A section that shows some customer reviews and blog entries that would link to my reviews page and blog to read more.

And finally a contact us section with my details, social media links and site map.

***
I also need to draw attention to where in the UK my services cover. I was therefore thinking perhaps we could use a picture to demonstrate this where it highlights Wiltshire, Oxfordshire, Berkshire and London on a map thereby demonstrating our areas covered. I have found several English county maps when searching on Google but I'm not sure how to highlight the areas I cover (or dull out the areas I don't) so if you have any ideas on this, I'd really like it incorporated. Thanks. (by the way, for those of you not familiar with English counties, the ones I cover are often abbreviated to Wilts, Oxon, Berks, London, so if you find a suitable map with those names on rather than the full names, you'll know what they are!)

I've found an image of the county map which might work well. I was wondering whether we might somehow grey out the counties I don't cover and just keep the ones I do as mentioned above and then crop it into perhaps a shadowed circle? I've attached a screenshot to the brief.
Updates

I've decided on the tag-line "Creating exquisite occasions today for amazing memories tomorrow" so if that could be included somewhere that would be great. I also need to draw attention to where in the UK my services cover. I was therefore thinking perhaps we could use a picture to demonstrate this where it highlights Wiltshire, Oxfordshire, Berkshire and London on a map thereby demonstrating our areas covered. I have found several English county maps when searching on Google but I'm not sure how to highlight the areas I cover (or dull out the areas I don't) so if you have any ideas on this, I'd really like it incorporated. Thanks. Added Wednesday, June 24, 2015

Target Market(s)

Predominately women aged 25-55

Industry/Entity Type

Wedding Planner

Number of Pages Required

1 page

Font styles to use
Sans Serif
Script

Requirements
Nice to have
• I'd like to see how the colour theme of purple and perhaps a little gold (maybe as a font colour) look against a white background. I've mentioned the Pantone colours in the brief above.
• I've attached a screenshot of a webpage with gold writing in and fonts that I like. Perhaps it could give you inspiration?
Should not have
• I really don't like the font QUILLORA so please done use that.

```html
<!DOCTYPE html>
<html lang="en">
<head>
<meta charset="utf-8">
<title>Silver Fern Gatherings</title>
<link href="https://fonts.googleapis.com/css2?family=Roboto:wght@300&display=swap" rel="stylesheet">
<style>
  :root {
    --purple: #9c22b4;
    --gold: #e2a955;
    --cream: #f7efe0;
    --white: #ffffff;
  }
  * { margin: 0; padding: 0; box-sizing: border-box; }
  html, body { width: 1200px; height: 853px; overflow: hidden; background: var(--white); }
  body { font-family: "Roboto", "Helvetica Neue", Arial, sans-serif; font-weight: 300; position: relative; }

  .brand { position: absolute; left: 24px; top: 30px; display: flex; align-items: center; gap: 12px; }
  .brand-dot { width: 56px; height: 56px; border-radius: 50%; border: 2px solid var(--purple); }
  .brand-name { color: var(--purple); font-size: 27px; letter-spacing: 0.5px; white-space: nowrap; }

  .main-nav { position: absolute; top: 34px; right: 46px; display: flex; gap: 25px; }
  .main-nav a { color: var(--purple); text-decoration: none; font-size: 25px; letter-spacing: -0.5px; white-space: nowrap; }

  .hero { position: absolute; left: 89px; top: 102px; width: 990px; height: 491px; overflow: hidden; }
  .hero-photo {
    position: absolute; inset: 0;
    background:
      radial-gradient(ellipse 28% 55% at 64% 60%, #cfa968 0%, #e6cfa2 45%, rgba(240,228,205,0) 100%),
      linear-gradient(100deg, #fbf7f0 0%, #f3e9d8 40%, #efe2c9 70%, #f6efe3 100%);
  }
  .hero-title {
    position: absolute; left: 39px; top: 156px; font-weight: 300; white-space: nowrap;
    color: var(--gold); font-size: 38px; line-height: 45px; letter-spacing: -0.5px;
  }

  .areas { position: absolute; top: 606px; left: 0; width: 1200px; height: 30px; }
  .areas span { position: absolute; transform: translateX(-50%); color: var(--gold); font-size: 22px; letter-spacing: -0.4px; white-space: nowrap; }

  .review-avatar { position: absolute; width: 158px; height: 158px; border-radius: 50%; border: 4px solid var(--gold);
    background: radial-gradient(circle at 50% 40%, #e8c79a 0%, #b98955 60%, #8e6a46 100%); }
  .review-quote { position: absolute; color: var(--purple); font-size: 19.5px; line-height: 26.7px; letter-spacing: -0.2px; white-space: nowrap; }
  .review-name, .review-role { position: absolute; color: var(--gold); font-size: 22px; line-height: 28px; letter-spacing: -0.4px; white-space: nowrap; }
</style>
</head>
<body>
  <header>
    <div class="brand">
      <span class="brand-dot"></span>
      <span class="brand-name">Silver Fern Gatherings</span>
    </div>
    <nav class="main-nav">
      <a href="#events">Events</a>
      <a href="#about">About</a>
    </nav>
  </header>

  <section class="hero">
    <div class="hero-photo" role="img" aria-label="Champagne bottle in a gold ice bucket with a glass, wedding dress softly blurred behind"></div>
    <h1 class="hero-title">Lorem Ipsum Amet,<br>Consectetur Adipiscing<br>Elit Dolor Set</h1>
  </section>

  <nav class="areas">
    <span style="left:278px">Oxfordshire</span>
    <span style="left:513px">Wiltshire</span>
    <span style="left:726px">Berkshire</span>
    <span style="left:940px">London</span>
  </nav>

  <section class="review">
    <div class="review-avatar" role="img" aria-label="Portrait of the reviewing wedding client" style="left:95px;top:650px"></div>
    <p class="review-quote" style="left:264px;top:652px">“Lorem ipsum dolor sit amet, consectetur adipiscing elit. Cras in turpis ultrices tortor<br>eleifend tempor pulvinar vitae metus. Praesent tempus, nibh ut lacinia semper, ipsum<br>neque iaculis enim, eget eleifend tellus nisl vel eros. Aliquam diam nulla, viverra ut eros et,<br>porttitor semper mauris.”</p>
    <p class="review-name" style="left:264px;top:759px">Jane Doe</p>
    <p class="review-role" style="left:264px;top:787px">Wedding Client</p>
  </section>

  <section class="review">
    <p class="review-quote" style="left:164px;top:829px">“Lorem ipsum dolor sit amet, consectetur adipiscing elit. Cras in turpis ultrices tortor</p>
    <div class="review-avatar" role="img" aria-label="Portrait of the reviewing client" style="left:940px;top:826px"></div>
  </section>
</body>
</html>
```